Venlox - Property Management Company Listings - PSD / uncoded only

Our site simply connects property owners with property managers. I’m asking you to create 2 pages, 1 homepage and 1 page that lists of property management companies. Build with Responsive Design in mind. PSD/uncoded files only. Help us create a great site!
Example competitor sites:
http://www.everyestatehelp.example/
http://www.tendyourlots.example/
Inspired by these sites:
http://www.quorvik.example/
http://www.bespokely.example/
http://www.coinwire.example/
https://www.tripboard.example/
I've attached the logo as well as 2 picture files that you can consider using.
• Venlox Logo Colors: Yellow: HTML code: #FBC30A, RGB code: R: 251 G: 195 B: 10 Grey: HTML code: #4E4C4D, RGB code: R: 78 G: 76 B: 77
• The picture files are optional.
o One picture is of houses and neighborhood.
o The other is of a professional woman on the phone. Please do not use the professional woman as a large primary image. You can use the professional woman photo as a smaller photo and not the main photo.
• Please bring your own pictures and graphics too. Don't feel like you need to use mine.
Thank you!

```html
<!DOCTYPE html>
<html lang="en">
<head>
<meta charset="utf-8">
<title>Venlox – Arlington Property Managers</title>
<link rel="stylesheet" href="https://fonts.googleapis.com/css2?family=Exo+2:wght@400;500;600&family=Roboto:wght@400;500;700&display=swap">
<style>
  :root{
    --yellow:#fbc30a;
    --grey:#4e4c4d;
    --navy:#1e3f7a;
    --blue:#1a8cf0;
    --blue-dark:#0f6fc4;
    --page:#f3f4f6;
    --band:#e7ecf0;
    --card:#ffffff;
    --card-line:#dfe3e7;
    --text:#3a3a3a;
    --footer:#676767;
    --search-panel:#d9e1e7;
  }
  *{box-sizing:border-box;margin:0;padding:0}
  html,body{width:678px;height:1200px;overflow:hidden}
  body{background:var(--page);font-family:"Roboto",Arial,sans-serif;color:var(--text);position:relative}

  .site-header{position:absolute;top:0;left:0;width:678px;height:54px;background:#fff}
  .brand{position:absolute;left:114px;top:16px;display:flex;align-items:center;gap:5px}
  .brand-mark{width:10px;height:10px;background:var(--yellow)}
  .brand-name{font-family:"Exo 2",sans-serif;font-weight:600;font-size:20px;color:var(--grey);line-height:1}
  .brand-tagline{position:absolute;left:188px;top:20px;font-family:"Exo 2",sans-serif;font-size:9px;line-height:10px;color:var(--grey)}
  .main-nav{position:absolute;top:24px;right:113px;display:flex;gap:11px;font-family:"Exo 2",sans-serif;font-size:8.3px;color:var(--grey);letter-spacing:-.1px}

  .hero-band{position:absolute;top:54px;left:0;width:678px;height:64px;background:var(--band);text-align:center;font-family:"Exo 2",sans-serif;color:#111}
  .hero-title{margin-top:11px;font-size:16px;font-weight:500;letter-spacing:.2px}
  .hero-sub{margin-top:3px;font-size:11.5px}
  .hero-sub strong{font-size:15px;font-weight:600}

  .listings{position:absolute;top:130px;left:114px;width:450px}
  .listing{height:104px;margin-bottom:7px;background:var(--card);border:1px solid var(--card-line);border-bottom:2px solid var(--yellow);position:relative;padding:13px 110px 0 13px}
  .listing-name{font-family:"Exo 2",sans-serif;font-size:16.5px;font-weight:500;color:var(--navy);letter-spacing:.1px;line-height:20px}
  .listing-text{margin-top:4px;font-size:6.6px;line-height:11.4px;color:#444;width:316px}
  .listing-link{position:absolute;left:13px;top:83px;font-size:6.5px;font-weight:700;color:#222}
  .consult-btn{position:absolute;right:9px;top:10px;width:101px;height:26px;background:var(--blue);border-bottom:2px solid var(--blue-dark);color:#fff;font-family:"Exo 2",sans-serif;font-size:8.5px;font-weight:600;display:flex;align-items:center;justify-content:center}

  .search-area{position:absolute;top:1030px;left:0;width:678px;height:108px;background:#eceff2}
  .search-panel{position:absolute;left:142px;top:13px;width:393px;height:87px;background:var(--search-panel);border:1px solid #c9d1d7}
  .field{position:absolute;top:11px;height:21px;background:#fff;border:1px solid #cfd4d8;font-size:8px;color:#333;display:flex;align-items:center;padding-left:12px}
  .field-type{left:24px;width:153px}
  .field-zip{left:182px;width:79px;padding-left:7px}
  .field-type svg{position:absolute;right:5px;top:4px}
  .search-btn{position:absolute;left:316px;top:11px;width:87px;height:21px;background:var(--blue);border-bottom:2px solid var(--blue-dark);color:#fff;font-family:"Exo 2",sans-serif;font-size:9px;font-weight:600;display:flex;align-items:center;justify-content:center}
  .search-note{position:absolute;top:52px;left:0;width:100%;text-align:center;font-size:8.3px;line-height:12px;color:#666}

  .site-footer{position:absolute;top:1138px;left:0;width:678px;height:62px;background:var(--footer);border-top:3px solid var(--yellow)}
  .footer-nav{display:flex;justify-content:center;margin-top:14px;font-size:7.5px;font-weight:500;color:#fff}
  .footer-nav span{padding:0 8px;border-left:1px solid #999}
  .footer-nav span:first-child{border-left:none}
  .footer-rule{width:400px;margin:7px auto 0;border-top:1px solid #7a7a7a}
  .copyright{text-align:center;margin-top:5px;font-size:7px;color:#ddd}
</style>
</head>
<body>
  <header class="site-header">
    <div class="brand"><span class="brand-mark"></span><span class="brand-name">Venlox</span></div>
    <div class="brand-tagline">Rental Care Connections<br>Made Easy</div>
    <nav class="main-nav"><span>HOME</span><span>ARE YOU A PROPERTY MANAGER?</span><span>CONTACT US</span></nav>
  </header>

  <section class="hero-band">
    <h1 class="hero-title">22204 - YOUR NEIGHBORHOOD ARLINGTON PROPERTY MANAGERS</h1>
    <p class="hero-sub">SPECIALIZING IN SINGLE HOME OR CONDO <strong>($300 TO $500K)</strong></p>
  </section>

  <main class="listings">
    <article class="listing"><h2 class="listing-name">KEYSTONE RENTAL CARE PROS</h2><p class="listing-text">This is a sample version of Lorem Ipsum. Proin gravida nibh vel velit auctor aliquet. Aenean sollicitudin, lorem quis bibendum auctor, nisi elit consequat ipsum, nec sagittis sem nibh id elit. Duis sed odio sit amet nibh vulputate cursus a sit amet mauris.</p><span class="listing-link">VIEW FULL COMPANY PROFILE</span><span class="consult-btn">FREE CONSULTATION</span></article>
    <article class="listing"><h2 class="listing-name">KEYSTONE RENTAL CARE PROS</h2><p class="listing-text">This is a sample version of Lorem Ipsum. Proin gravida nibh vel velit auctor aliquet. Aenean sollicitudin, lorem quis bibendum auctor, nisi elit consequat ipsum, nec sagittis sem nibh id elit. Duis sed odio sit amet nibh vulputate cursus a sit amet mauris.</p><span class="listing-link">VIEW FULL COMPANY PROFILE</span><span class="consult-btn">FREE CONSULTATION</span></article>
    <article class="listing"><h2 class="listing-name">KEYSTONE RENTAL CARE PROS</h2><p class="listing-text">This is a sample version of Lorem Ipsum. Proin gravida nibh vel velit auctor aliquet. Aenean sollicitudin, lorem quis bibendum auctor, nisi elit consequat ipsum, nec sagittis sem nibh id elit. Duis sed odio sit amet nibh vulputate cursus a sit amet mauris.</p><span class="listing-link">VIEW FULL COMPANY PROFILE</span><span class="consult-btn">FREE CONSULTATION</span></article>
    <article class="listing"><h2 class="listing-name">KEYSTONE RENTAL CARE PROS</h2><p class="listing-text">This is a sample version of Lorem Ipsum. Proin gravida nibh vel velit auctor aliquet. Aenean sollicitudin, lorem quis bibendum auctor, nisi elit consequat ipsum, nec sagittis sem nibh id elit. Duis sed odio sit amet nibh vulputate cursus a sit amet mauris.</p><span class="listing-link">VIEW FULL COMPANY PROFILE</span><span class="consult-btn">FREE CONSULTATION</span></article>
    <article class="listing"><h2 class="listing-name">KEYSTONE RENTAL CARE PROS</h2><p class="listing-text">This is a sample version of Lorem Ipsum. Proin gravida nibh vel velit auctor aliquet. Aenean sollicitudin, lorem quis bibendum auctor, nisi elit consequat ipsum, nec sagittis sem nibh id elit. Duis sed odio sit amet nibh vulputate cursus a sit amet mauris.</p><span class="listing-link">VIEW FULL COMPANY PROFILE</span><span class="consult-btn">FREE CONSULTATION</span></article>
    <article class="listing"><h2 class="listing-name">KEYSTONE RENTAL CARE PROS</h2><p class="listing-text">This is a sample version of Lorem Ipsum. Proin gravida nibh vel velit auctor aliquet. Aenean sollicitudin, lorem quis bibendum auctor, nisi elit consequat ipsum, nec sagittis sem nibh id elit. Duis sed odio sit amet nibh vulputate cursus a sit amet mauris.</p><span class="listing-link">VIEW FULL COMPANY PROFILE</span><span class="consult-btn">FREE CONSULTATION</span></article>
    <article class="listing"><h2 class="listing-name">KEYSTONE RENTAL CARE PROS</h2><p class="listing-text">This is a sample version of Lorem Ipsum. Proin gravida nibh vel velit auctor aliquet. Aenean sollicitudin, lorem quis bibendum auctor, nisi elit consequat ipsum, nec sagittis sem nibh id elit. Duis sed odio sit amet nibh vulputate cursus a sit amet mauris.</p><span class="listing-link">VIEW FULL COMPANY PROFILE</span><span class="consult-btn">FREE CONSULTATION</span></article>
    <article class="listing"><h2 class="listing-name">KEYSTONE RENTAL CARE PROS</h2><p class="listing-text">This is a sample version of Lorem Ipsum. Proin gravida nibh vel velit auctor aliquet. Aenean sollicitudin, lorem quis bibendum auctor, nisi elit consequat ipsum, nec sagittis sem nibh id elit. Duis sed odio sit amet nibh vulputate cursus a sit amet mauris.</p><span class="listing-link">VIEW FULL COMPANY PROFILE</span><span class="consult-btn">FREE CONSULTATION</span></article>
  </main>

  <section class="search-area">
    <div class="search-panel">
      <div class="field field-type">Select Your Property Type
        <svg width="13" height="13" viewBox="0 0 13 13" aria-hidden="true"><circle cx="6.5" cy="6.5" r="6.5" fill="#fbc30a"/><path d="M3.8 5.2h5.4L6.5 8.4z" fill="#4e4c4d"/></svg>
      </div>
      <div class="field field-zip">In Zipcode</div>
      <div class="search-btn">SEARCH</div>
      <p class="search-note">Search our directory to find experienced and professional property<br>management companies that meet your needs.</p>
    </div>
  </section>

  <footer class="site-footer">
    <nav class="footer-nav"><span>Are you a Property Manager?</span><span>About Us</span><span>Contact Us</span><span>Terms of Use</span><span>Privacy Policy</span><span>Site Map</span></nav>
    <div class="footer-rule"></div>
    <p class="copyright">Copyright © 2014, Venlox, All Rights Reserved</p>
  </footer>
</body>
</html>
```